Real Estate and Property Management Company needs new listings

We need a business card for our company, Dorsell Estates & Property Management. We maximize financial returns on residential investment properties. By evaluating the current value and health of a property, we devise a financial plan to rehabilitate the property while earning an income over a period of years for rental properties, or suggest meaningful updates and improvements to ensure maximum payout on sales properties.
We would like to see our business cards with the colors black and metallic burgundy. The final design should communicate management and financial growth.

Target Market(s)

Home Owners of single family, detatched residential homes.

Industry/Entity Type

Business

Contact Information for Business Card

Side 1: Maren Dorsell
Broker, Owner
Maren@DorsellEstates.example
555-284-7719 (Cell)
555-731-4062 (Office)
Please incorporate in the design of side 1 that we have been in business for 40 years, along with communicating sales and management.
Side 2: Tessa Dorsell
Property Manager
Tessa@DorsellEstates.example
555-284-7745 (Cell)
555-731-4062 (Office)
Please incorporate that we are a family owner and operated company on side 2.

Font styles to use
Serif

Requirements
Must have
• Elegant, feminine design of metallic burgundy on black on double sided card.
Nice to have
• I would like to see some consistency of design on the front and back of the card, with perhaps a bold, thick line of burgundy on the right, vertical side. I would also like the black card stock to have some geometrical design or texture.
Should not have
• Any of the colors provided below. I cannot choose burgundy, which is the color for our business. Is this the only color selection available?

```html
<!DOCTYPE html>
<html lang="en">
<head>
<meta charset="utf-8">
<title>Dorsell Estates &amp; Property Management — Business Cards</title>
<link rel="stylesheet" href="https://fonts.googleapis.com/css2?family=Cinzel:wght@400;600&family=Playfair+Display&family=Open+Sans:ital,wght@0,400;0,700;1,700&display=swap">
<style>
  :root {
    --backdrop: #d9d9d9;
    --card-black: #222222;
    --cream: #ece3d5;
    --burgundy-dark: #5e0f1b;
    --burgundy: #8f1a2d;
    --burgundy-light: #a52238;
    --ink: #1e1e1e;
    --title-red: #9a1b2c;
    --muted: #cfcfcf;
  }
  * { margin: 0; padding: 0; box-sizing: border-box; }
  html, body { width: 1200px; height: 900px; overflow: hidden; }
  body { background: var(--backdrop); position: relative; font-family: "Open Sans", sans-serif; }

  .card {
    position: absolute;
    width: 540px;
    height: 310px;
    background: var(--card-black);
    box-shadow: 0 2px 6px rgba(0,0,0,0.25);
  }
  .card--broker { left: 60px; top: 100px; }
  .card--manager { left: 600px; top: 490px; }

  .cream-strip { position: absolute; top: 22px; width: 26px; height: 266px; background: var(--cream); }

  .burgundy-band {
    position: absolute; top: 0; height: 100%;
    background: linear-gradient(90deg, var(--burgundy-dark) 0%, var(--burgundy) 35%, var(--burgundy-light) 55%, var(--burgundy) 75%, var(--burgundy-dark) 100%);
  }
  .burgundy-band::before, .burgundy-band::after {
    content: ""; position: absolute; top: 0; width: 4px; height: 100%; background: var(--card-black);
  }
  .burgundy-band::before { left: 10px; }
  .burgundy-band::after { right: 10px; }

  .company-panel {
    position: absolute; left: 60px; top: 92px; width: 195px; height: 126px;
    background: var(--card-black);
    border-top: 4px solid var(--card-black);
    display: flex; flex-direction: column; justify-content: center; align-items: center;
    text-align: center; color: var(--cream);
    box-shadow: 0 -8px 0 -4px var(--burgundy), 0 8px 0 -4px var(--burgundy);
  }
  .company-name { font-family: "Playfair Display", serif; font-size: 17px; line-height: 1.3; }
  .company-tag { font-family: "Playfair Display", serif; font-size: 11px; letter-spacing: 3px; margin-top: 8px; }

  .contact-panel {
    position: absolute; top: 22px; height: 266px; width: 270px;
    background: var(--cream); color: var(--ink);
  }
  .card--broker .contact-panel { left: 252px; }
  .card--manager .contact-panel { left: 25px; height: 244px; }

  .person-name {
    position: absolute; top: 34px; width: 100%; text-align: center;
    font-family: "Cinzel", serif; font-weight: 600; font-size: 21px; letter-spacing: 1px;
  }
  .person-role {
    position: absolute; top: 64px; width: 100%; text-align: center;
    font-size: 11px; font-weight: 700; color: var(--title-red); letter-spacing: 0.5px;
  }
  .flourish {
    position: absolute; top: 86px; left: 85px; width: 100px; height: 14px;
    background: linear-gradient(90deg, transparent, rgba(60,50,45,0.35), transparent);
    border-radius: 7px;
  }
  .contact-line {
    position: absolute; font-size: 10px; font-weight: 700; font-style: italic; letter-spacing: 2px;
    padding-top: 4px; border-top: 1.5px solid var(--ink);
    text-align: center;
  }
  .contact-line svg { position: absolute; top: -22px; left: 50%; margin-left: -9px; width: 18px; height: 20px; }
  .contact-line--cell { left: 22px; top: 140px; width: 96px; }
  .contact-line--office { right: 22px; top: 178px; width: 96px; }
  .contact-line--email { left: 50%; margin-left: -90px; top: 214px; width: 180px; font-size: 8.5px; letter-spacing: 0.3px; }
  .card--manager .contact-line--email { top: 198px; }

  .experience {
    position: absolute; left: 28px; bottom: 10px;
    color: var(--muted); font-size: 13px; letter-spacing: 0.3px;
  }
</style>
</head>
<body>

<section class="card card--broker" aria-label="Broker business card">
  <div class="cream-strip" style="left:28px;"></div>
  <div class="burgundy-band" style="left:65px; width:180px;"></div>
  <div class="company-panel">
    <p class="company-name">Dorsell Estates &amp;<br>Property Management</p>
    <p class="company-tag">Family Business</p>
  </div>
  <div class="contact-panel">
    <h1 class="person-name">Maren Dorsell</h1>
    <p class="person-role">Broker, Owner</p>
    <div class="flourish" role="img" aria-label="Decorative flourish under the title"></div>
    <p class="contact-line contact-line--cell">
      <svg viewBox="0 0 18 20"><rect x="4" y="1" width="10" height="18" rx="2" fill="#1e1e1e"/><rect x="6" y="4" width="6" height="10" fill="#ece3d5"/></svg>
      555-284-7719
    </p>
    <p class="contact-line contact-line--office">
      <svg viewBox="0 0 18 20"><path d="M4 3c2-1 3 0 4 2l-1 2c0 1 2 4 4 5l2-1c2 1 3 2 2 4-1 2-3 2-5 1C6 14 3 9 3 6c0-1 0-2 1-3z" fill="#1e1e1e"/></svg>
      555-731-4062
    </p>
    <p class="contact-line contact-line--email">
      <svg viewBox="0 0 18 20"><path d="M1 9 9 3l8 6v9H1z" fill="#1e1e1e"/><path d="M3 10l6 4 6-4" stroke="#ece3d5" stroke-width="1.2" fill="none"/></svg>
      Maren@DorsellEstates.example
    </p>
  </div>
</section>

<section class="card card--manager" aria-label="Property manager business card">
  <div class="contact-panel">
    <h2 class="person-name">Tessa Dorsell</h2>
    <p class="person-role">Property Manager</p>
    <div class="flourish" role="img" aria-label="Decorative flourish under the title"></div>
    <p class="contact-line contact-line--cell">
      <svg viewBox="0 0 18 20"><rect x="4" y="1" width="10" height="18" rx="2" fill="#1e1e1e"/><rect x="6" y="4" width="6" height="10" fill="#ece3d5"/></svg>
      555-284-7745
    </p>
    <p class="contact-line contact-line--office" style="top:166px;">
      <svg viewBox="0 0 18 20"><path d="M4 3c2-1 3 0 4 2l-1 2c0 1 2 4 4 5l2-1c2 1 3 2 2 4-1 2-3 2-5 1C6 14 3 9 3 6c0-1 0-2 1-3z" fill="#1e1e1e"/></svg>
      555-731-4062
    </p>
    <p class="contact-line contact-line--email">
      <svg viewBox="0 0 18 20"><path d="M1 9 9 3l8 6v9H1z" fill="#1e1e1e"/><path d="M3 10l6 4 6-4" stroke="#ece3d5" stroke-width="1.2" fill="none"/></svg>
      Tessa@DorsellEstates.example
    </p>
  </div>
  <p class="experience">40 years of experience...</p>
  <div class="burgundy-band" style="left:312px; width:140px;"></div>
  <div class="cream-strip" style="left:466px;"></div>
</section>

</body>
</html>
```